Wealth Advising Business Cards and Stationery
Brightmoor Capital Partners
Wealth Advising Business Cards and Stationery - Financial Services
Creative Brief
Simple
Colin Ashdown
Founder - Managing Director
4419 Hollis Crest Road, Suite 820, Larkmont Falls 10820
colin@brightmoorcapitalpartners.example
www.brightmoorcapitalpartners.example
I'd like the logo to be on one side and the contact information on the other.

```html
<!DOCTYPE html>
<html lang="en">
<head>
<meta charset="utf-8">
<title>Brightmoor Capital Partners – Business Card</title>
<link href="https://fonts.googleapis.com/css2?family=Cinzel:wght@400;500&family=Open+Sans:wght@400;600&display=swap" rel="stylesheet">
<style>
  :root {
    --brand-blue: #1f4f9c;
    --brand-blue-deep: #173f82;
    --card-white: #ffffff;
    --ink: #3b4350;
    --backdrop: #2b2b2d;
    --backdrop-light: #3a3a3c;
  }
  * { box-sizing: border-box; margin: 0; padding: 0; }
  html, body { width: 1200px; height: 901px; overflow: hidden; }
  body {
    background: radial-gradient(ellipse at 50% 40%, var(--backdrop-light), var(--backdrop) 75%);
    display: flex; align-items: center; justify-content: center; gap: 40px;
  }
  .card {
    width: 540px; height: 309px; position: relative; flex: none;
    box-shadow: 0 12px 30px rgba(0,0,0,.45);
  }
  /* Contact side */
  .card--front { background: var(--card-white); }
  .card--front::before, .card--front::after {
    content: ""; position: absolute; top: 0; bottom: 0; width: 8px; background: var(--brand-blue);
  }
  .card--front::before { left: 0; }
  .card--front::after { right: 0; }
  .wordmark {
    font-family: "Cinzel", serif; font-weight: 400; color: var(--brand-blue);
    text-transform: uppercase; line-height: 1.15; letter-spacing: .04em;
  }
  .card--front .wordmark { position: absolute; left: 34px; top: 40px; font-size: 17px; }
  .divider { position: absolute; left: 212px; top: 40px; width: 1px; height: 150px; background: var(--brand-blue); }
  .contact { position: absolute; left: 230px; top: 36px; right: 26px; font-family: "Open Sans", sans-serif; color: var(--ink); }
  .contact__name { font-family: "Cinzel", serif; font-size: 22px; color: var(--brand-blue); letter-spacing: .03em; white-space: nowrap; }
  .contact__title { font-size: 11px; margin: 2px 0 12px; }
  .contact__address { font-size: 11px; line-height: 1.45; margin-bottom: 8px; }
  .contact__line { display: flex; align-items: center; gap: 7px; font-size: 11px; line-height: 1.6; white-space: nowrap; }
  .contact__line svg { width: 10px; height: 10px; fill: var(--brand-blue); flex: none; }
  /* Logo side */
  .card--back { background: linear-gradient(135deg, var(--brand-blue), var(--brand-blue-deep)); display: flex; align-items: center; justify-content: center; }
  .card--back .wordmark { color: var(--card-white); font-size: 30px; text-align: center; }
</style>
</head>
<body>
  <section class="card card--front" aria-label="Business card, contact side">
    <div class="wordmark">Brightmoor<br>Capital Partners</div>
    <div class="divider"></div>
    <div class="contact">
      <div class="contact__name">Colin Ashdown</div>
      <div class="contact__title">Founder - Managing Director</div>
      <div class="contact__address">4419 Hollis Crest Road,<br>Suite 820, Larkmont Falls 10820</div>
      <div class="contact__line">
        <svg viewBox="0 0 10 10"><path d="M2 0.5 L4 2.8 L3 4 Q4.5 6 6 7 L7.2 6 L9.5 8 L8 9.6 Q4 9 0.5 2 Z"/></svg>
        <span>555 010 4821</span>
      </div>
      <div class="contact__line">
        <svg viewBox="0 0 10 10"><path d="M2 0.5 L4 2.8 L3 4 Q4.5 6 6 7 L7.2 6 L9.5 8 L8 9.6 Q4 9 0.5 2 Z"/></svg>
        <span>555 010 7736</span>
      </div>
      <div class="contact__line">
        <svg viewBox="0 0 10 10"><rect x="0.5" y="2" width="9" height="6.5" rx="1"/></svg>
        <span>colin@brightmoorcapitalpartners.example</span>
      </div>
      <div class="contact__line">
        <svg viewBox="0 0 10 10"><circle cx="5" cy="5" r="4.5"/></svg>
        <span>www.brightmoorcapitalpartners.example</span>
      </div>
    </div>
  </section>
  <section class="card card--back" aria-label="Business card, logo side">
    <div class="wordmark">Brightmoor<br>Capital Partners</div>
  </section>
</body>
</html>
```